Letterhead for small civil engineer company

We need bold and modern design for company letterhead in MS word. It needs to have company logo and company info. Somewhere in the upper right part of document needs to be space for "recever" and the documents starts with, example, "SUBJECT: CIVIL ENGINEER LETTERHEAD".

in the bottom part of document needs to be signature and date.

Company info: Veltrana d.o.o., Lipovac 15, Lipovac (Općina Brdarić), OIB 47396028154, www.veltrana.hr, info@veltrana.hr

Email of document sender needs to be somewhere if document, exapmle xyz@veltrana.hr

Target Market(s)

Civil engineer company and projects

Industry/Entity Type

Civil engineer

Font styles to use
Serif

Colors
F0912C
F2A743
F7CA91
FBE8D2
FDF5EE

Requirements
Must have
• Company logo and company info
Nice to have
• Moder and clean design
Should not have
• Too much details

```html
<!DOCTYPE html>
<html lang="hr">
<head>
<meta charset="UTF-8">
<title>Veltrana d.o.o. – Letterhead</title>
<link rel="stylesheet" href="https://fonts.googleapis.com/css2?family=Jost:wght@400;500&family=Hind:wght@400&display=swap">
<style>
  :root {
    --accent: #e8914a;
    --frame: #6f6f72;
    --label: #6d6e70;
    --rule: #8a8a8c;
    --paper: #fdfdfd;
  }
  * { margin: 0; padding: 0; box-sizing: border-box; }
  html, body { width: 848px; height: 1200px; overflow: hidden; background: var(--paper); }
  .sheet { position: relative; width: 848px; height: 1200px; background: var(--paper); }

  .brand-square {
    position: absolute; left: 96px; top: 48px;
    width: 73px; height: 73px;
    border: 2px solid var(--frame);
  }
  .brand-name {
    position: absolute; left: 30px; top: 124px;
    width: 208px; text-align: center;
    font-family: "Jost", sans-serif; font-weight: 500;
    font-size: 30px; letter-spacing: 1.5px;
    color: var(--accent); line-height: 1;
  }

  .company-info {
    position: absolute; left: 555px; top: 72px;
    font-family: "Jost", sans-serif; font-weight: 400;
    font-size: 16.5px; line-height: 19.5px;
    color: var(--accent);
  }

  .field {
    position: absolute; display: flex; align-items: flex-end;
    font-size: 16.5px; color: var(--label); line-height: 1;
  }
  .field .line { border-bottom: 1px solid var(--rule); margin-left: 4px; height: 1px; }
  .field--left { font-family: "Hind", sans-serif; letter-spacing: 0.6px; }
  .field--right { font-family: "Jost", sans-serif; }

  .receiver-name { left: 31px; top: 1063px; }
  .receiver-name .line { width: 315px; }
  .receiver-address { left: 31px; top: 1099px; }
  .receiver-address .line { width: 291px; margin-left: 10px; }
  .sender-email { left: 31px; top: 1135px; }
  .sender-email .line { width: 330px; }

  .date { left: 601px; top: 1094px; }
  .date .line { width: 139px; margin-left: 5px; }
  .signature { left: 601px; top: 1127px; }
  .signature .line { width: 139px; margin-left: 5px; }
</style>
</head>
<body>
<main class="sheet">
  <header>
    <div class="brand-square" aria-hidden="true"></div>
    <div class="brand-name">VELTRANA</div>
    <address class="company-info" style="font-style:normal">
      Veltrana d.o.o., Lipovac 15,<br>
      Lipovac (Općina Brdarić),<br>
      OIB 47396028154<br>
      www.veltrana.hr | info@veltrana.hr
    </address>
  </header>

  <footer>
    <div class="field field--left receiver-name"><span>Receiver Name:</span><span class="line"></span></div>
    <div class="field field--left receiver-address"><span>Receiver Address:</span><span class="line"></span></div>
    <div class="field field--left sender-email"><span>Sender Email:</span><span class="line"></span></div>
    <div class="field field--right date"><span>Date:</span><span class="line"></span></div>
    <div class="field field--right signature"><span>Signature:</span><span class="line"></span></div>
  </footer>
</main>
</body>
</html>
```